Bulldog themed background for Real Estate Purchase Letter

I need a phantom background or watermark on a standard 8 1/2" x 11" paper. I am going to put a letter over the background. I want a bulldog theme that is cute, funny and original. This letter is for a real estate project and we want to capture the person sub-consciously . Attached is my personal dogs. If you want to use them you can but not required. I have attached the letter that I am trying to emulate. I want bulldogs not horses.

Target Market(s)

45 years old and higher

Industry/Entity Type

Real Estate

Font styles to use
Serif
Sans Serif

Colors

Designer to choose colors to be used in the design.

Requirements
Must have
• fun, happiness, reassuring,
Should not have
• violence, negativity, unhappy

```html
<!DOCTYPE html>
<html lang="en">
<head>
<meta charset="utf-8">
<title>Real Estate Purchase Letter</title>
<link rel="stylesheet" href="https://fonts.googleapis.com/css2?family=Montserrat:wght@600&family=Open+Sans:wght@300;400;600&display=swap">
<style>
  :root {
    --blue-deep: #0a4fc4;
    --blue-mid: #0a6fd6;
    --blue-sky: #14aee8;
    --ink: #3a3a3a;
    --ink-strong: #2b2b2b;
    --paper: #ffffff;
    --dog-warm: #b79a86;
    --dog-dark: #6e5a52;
    --dog-light: #e8e2dd;
  }
  html, body { margin: 0; padding: 0; overflow: hidden; background: var(--paper); }
  .letter {
    position: relative;
    width: 850px;
    height: 1200px;
    overflow: hidden;
    background: var(--paper);
    font-family: "Open Sans", Arial, sans-serif;
    font-weight: 300;
    color: var(--ink);
  }
  .backdrop-dogs {
    position: absolute;
    left: 0;
    top: 430px;
    width: 850px;
    height: 660px;
    background:
      radial-gradient(ellipse 200px 260px at 200px 330px, var(--dog-light) 0%, rgba(232,226,221,0) 100%),
      radial-gradient(ellipse 220px 300px at 640px 260px, var(--dog-dark) 0%, rgba(110,90,82,0) 100%),
      radial-gradient(ellipse 360px 330px at 420px 330px, var(--dog-warm) 0%, rgba(183,154,134,0) 100%);
    opacity: 0.28;
  }
  .waves { position: absolute; inset: 0; width: 850px; height: 1200px; }
  .agent-id {
    position: absolute;
    left: 67px;
    top: 48px;
    margin: 0;
    font-family: "Montserrat", Arial, sans-serif;
    font-weight: 600;
    font-size: 18px;
    line-height: 26px;
    color: #ffffff;
  }
  .recipient {
    position: absolute;
    left: 69px;
    top: 198px;
    margin: 0;
    font-size: 17.5px;
    line-height: 30.5px;
    font-weight: 400;
    color: var(--ink);
  }
  .recipient .name { font-weight: 600; color: var(--ink-strong); }
  .salutation {
    position: absolute;
    left: 69px;
    top: 330px;
    margin: 0;
    font-size: 17.5px;
    font-weight: 400;
  }
  .salutation strong { font-weight: 600; color: var(--ink-strong); }
  .body {
    position: absolute;
    left: 69px;
    top: 401px;
    width: 711px;
  }
  .body p {
    margin: 0 0 33px;
    font-size: 17.5px;
    line-height: 32.7px;
    text-align: justify;
    text-indent: 40px;
  }
  .body strong { font-weight: 600; color: var(--ink-strong); }
  .closing {
    position: absolute;
    left: 69px;
    top: 1025px;
    margin: 0;
    font-size: 17.5px;
    font-weight: 400;
  }
  .signature {
    position: absolute;
    left: 69px;
    top: 1101px;
    margin: 0;
    font-size: 17.5px;
    font-weight: 600;
    color: var(--ink-strong);
  }
</style>
</head>
<body>
<main class="letter">
  <div class="backdrop-dogs" role="img" aria-label="Faint watermark photo of two friendly bulldogs wearing bandanas"></div>

  <svg class="waves" viewBox="0 0 850 1200" aria-hidden="true">
    <path fill="var(--blue-sky)" d="M0,0 H548 C470,30 430,55 380,72 C300,100 220,110 140,130 C70,150 30,180 0,240 Z"/>
    <path fill="var(--blue-deep)" d="M0,0 H520 C450,25 410,50 360,65 C290,88 210,95 130,112 C60,128 25,160 0,215 Z"/>
    <path fill="var(--blue-sky)" d="M200,1200 C300,1150 400,1110 520,1080 C640,1050 720,1040 790,1000 C820,985 840,965 850,950 V1200 Z"/>
    <path fill="var(--blue-mid)" d="M222,1200 C320,1160 420,1125 530,1095 C650,1064 730,1055 800,1015 C825,1002 842,985 850,975 V1200 Z"/>
    <path fill="var(--blue-deep)" d="M300,1200 C400,1170 480,1140 580,1115 C690,1088 760,1075 850,1030 V1200 Z"/>
  </svg>

  <p class="agent-id">Real Estate Agent ID :<br>#0298471635</p>

  <p class="recipient"><span class="name">Mr. Sample Homeowner</span><br>4821 Maple Row<br>Lakeview FL 3412-0087</p>

  <p class="salutation">Dear <strong>First Name</strong></p>

  <section class="body">
    <p>I am writing you, because I am interested in purchasing your property located at <strong>4821 Maple Row Lakeview FL 3412-0087</strong> I live nearby in Brookhaven and I puschages properties throught the state of PA Currently I am working on projects in the neighbourhood, which is how I learned of your property.</p>
    <p>Please call me at <strong>(XXX) XXXX-Local#</strong> so I can tell you how we can buy your property quickly, with no hassels and most importantly, at a fair price. I purchase the hous directly from you so there are no real estate commissions or extra fees coming out of your pocket. Furthermore, I always make cash offers so you never have to worry about delays resulting from a buyer trying to qualify for a mortgage and wasting your valuable time.</p>
    <p>I'will be glade to personally tell you more about how we can work together. All call are completely confidential and there is no obligation whatsoever. Even if you are not intersted in selling at thing time call <strong>(xxx) xxxx-xxxx</strong>, so I can help you with determining the value of your property. You should also keep this letter for your future reference, since things in life have a tendency to change unexpectedly. Thanks you for your time and consideration and I look forward to speaking with you.</p>
  </section>

  <p class="closing">Sincerely,</p>
  <p class="signature">Dana Whitfield</p>
</main>
</body>
</html>
```